VORTA Diagnostics Pooling One Sheet

The process and concept for pooling is to target large populations of people; i.e. a school, prison, employer (where people are isolated by pods), then to test them all in one controllable group. By breaking down the pool size (ideally is 12 or 16 max) then when a positive pool pops up, the entity has the lab automatically reflex to test the whole pool to determine who is positive. During that exchange, several workflows could take place from the population that was being tested. This type of pooled testing is called Surveillance testing ,when it reflects, then it goes to Screening or Diagnostic testing.

The workflow is:
School/employer collects all patient information captured on a requisition form or electronically (w signature) and DOES NOT send to VORTA
School/employer collects individual specimens and labels them with a unique bar code (non-repeating and can include the DOB)
School/employer is responsible for housing and managing all the unique patient information for each individual specimen
School/employer delivers specimens to VORTA and School/employer directs VORTA what specimens are in what designated pool (one pool size for entire project)
When a pool is positive, VORTA notifies School/employer
When reflex testing in indicated for client, School/employer submits to VORTA on demand all patient information needed to process the reflexed option
VORTA reports back to School/employer in 12 hours the results of the retest
https://www.healthbureau-example.test/medical-devices/coronavirus-covid-19-and-medical-devices/pooled-sample-testing-and-screening-testing-covid-19
https://www.mediquestlabs.test/coronavirus-disease-covid-19/news/mediquest-receives-authorization-covid-19-sample-pooling

Target Market(s)

Schools, Universities, Employers

Font styles to use
Sans Serif

Colors
85acd3
85cae6
34a6d7

Requirements
Must have
• VORTA branded along with an elegant yet clinical feel. have all contact information for VORTA Diagnostics. Go to www.vortadx.test for all info

```html
<!DOCTYPE html>
<html lang="en">
<head>
<meta charset="utf-8">
<title>VORTA Diagnostics – Pool Testing</title>
<link rel="stylesheet" href="https://fonts.googleapis.com/css2?family=Barlow+Condensed:wght@600&family=Barlow+Semi+Condensed:ital,wght@0,400;0,600;0,700;1,400&family=Oswald:wght@500&display=swap">
<style>
  :root{
    --backdrop:#1b1718;
    --paper:#ffffff;
    --paper-tint:#eef3f4;
    --teal:#4aa3b8;
    --teal-dark:#2a8fa8;
    --ink:#2d3a40;
    --muted:#5b6468;
    --band-1:#3d9fb5;
    --band-2:#7cc3e1;
    --band-3:#1f8ba0;
    --band-4:#34a6d7;
    --band-5:#176f7d;
    --band-6:#1f84bb;
    --band-7:#135660;
  }
  *{margin:0;padding:0;box-sizing:border-box}
  html,body{width:1200px;height:1200px;overflow:hidden;background:var(--backdrop)}
  .sheet{position:absolute;left:214px;top:79px;width:804px;height:1040px;background:var(--paper);overflow:hidden;font-family:"Barlow Semi Condensed",sans-serif;color:var(--ink)}
  .header{position:absolute;left:0;top:0;width:804px;height:77px}
  .header > svg{position:absolute;left:0;top:0}
  .brand{position:absolute;left:28px;top:27px;display:flex;align-items:center;gap:10px}
  .brand-mark{width:26px;height:26px;background:var(--teal-dark)}
  .brand-name{font-size:28px;line-height:30px;font-weight:600;color:var(--teal-dark)}
  .title{position:absolute;right:84px;top:8px;font-family:"Oswald",sans-serif;font-weight:500;font-size:47px;color:#fff;letter-spacing:-.3px;line-height:60px}
  .intro{position:absolute;left:0;top:77px;width:804px;height:139px}
  .intro-art{position:absolute;left:28px;top:35px;width:83px;height:83px;border-radius:4px;background:linear-gradient(160deg,#d7eef3,#a9d8e3)}
  .intro-text{position:absolute;left:141px;top:27px;width:650px;font-size:12.6px;line-height:17.4px;color:#3a4449;white-space:nowrap}
  .steps{position:absolute;left:0;top:216px;width:804px;height:769px;background:var(--paper-tint)}
  .steps > svg{position:absolute;left:0;top:0}
  .step{position:absolute;left:0;height:89.5px;display:flex;align-items:center;color:#fff}
  .step-num{width:74px;padding-left:16px;font-family:"Barlow Condensed",sans-serif;font-size:48px;font-weight:600;line-height:1}
  .step-text{font-size:14px;line-height:17.4px;font-weight:400;white-space:nowrap}
  .step-text b{font-weight:700}
  .refs{position:absolute;left:38px;top:929px;font-size:11.6px;line-height:17px;font-style:italic;color:var(--muted);white-space:nowrap}
  .footer{position:absolute;left:0;top:985px;width:804px;height:55px}
  .footer > svg{position:absolute;left:0;top:0}
  .phone{position:absolute;left:57px;top:12px;font-size:21px;line-height:30px;font-weight:600;color:#fff}
  .web{position:absolute;left:490px;top:11px;display:flex;align-items:center;gap:11px;font-size:27px;line-height:32px;font-weight:700;color:#1c5f6e}
  .web-icon{flex:none;display:block}
</style>
</head>
<body>
<div class="sheet">

  <header class="header">
    <svg width="804" height="77" viewBox="0 0 804 77">
      <polygon points="332,0 352,0 396,77 376,77" fill="var(--teal)"/>
      <polygon points="370,0 804,0 804,77 414,77" fill="var(--teal)"/>
    </svg>
    <div class="brand"><span class="brand-mark"></span><span class="brand-name">VORTA Diagnostics</span></div>
    <h1 class="title">POOL TESTING</h1>
  </header>

  <section class="intro">
    <div class="intro-art" role="img" aria-label="Outline illustration of an office building with a group of people in front"></div>
    <p class="intro-text">The process and concept for pooling is to target large populations of people; i.e. a school, prison, employer (where people are<br>isolated by pods), then to test them all in one controllable group. By breaking down the pool size (ideally is 12 or 16 max) then<br>when a positive pool pops up, the entity has the lab automatically reflex to test the whole pool to determine who is positive.<br>During that exchange, several workflows could take place from the population that was being tested. This type of pooled testing<br>is called Surveillance testing, when it reflects, then it goes to Screening or Diagnostic testing.</p>
  </section>

  <section class="steps">
    <svg width="804" height="769" viewBox="0 0 804 769">
      <defs>
        <filter id="hex-shadow" x="-30%" y="-30%" width="160%" height="160%">
          <feDropShadow dx="0" dy="3" stdDeviation="4" flood-color="#000" flood-opacity=".22"/>
        </filter>
        <polygon id="hex-outer" points="0,-62 54,-31 54,31 0,62 -54,31 -54,-31"/>
        <polygon id="hex-inner" points="0,-49 43,-24.5 43,24.5 0,49 -43,24.5 -43,-24.5"/>
      </defs>
      <rect x="0" y="43"    width="417" height="89.5" fill="var(--band-1)"/>
      <rect x="0" y="132.5" width="537" height="89.5" fill="var(--band-2)"/>
      <rect x="0" y="222"   width="689" height="89.5" fill="var(--band-3)"/>
      <rect x="0" y="311.5" width="569" height="89.5" fill="var(--band-4)"/>
      <rect x="0" y="401"   width="449" height="89.5" fill="var(--band-5)"/>
      <rect x="0" y="490.5" width="651" height="89.5" fill="var(--band-6)"/>
      <rect x="0" y="580"   width="414" height="89.5" fill="var(--band-7)"/>

      <g transform="translate(417,88)"  filter="url(#hex-shadow)"><use href="#hex-outer" fill="#fff"/><use href="#hex-inner" fill="none" stroke="var(--band-1)" stroke-width="2"/></g>
      <g transform="translate(537,177)" filter="url(#hex-shadow)"><use href="#hex-outer" fill="#fff"/><use href="#hex-inner" fill="none" stroke="var(--band-2)" stroke-width="2"/></g>
      <g transform="translate(689,267)" filter="url(#hex-shadow)"><use href="#hex-outer" fill="#fff"/><use href="#hex-inner" fill="none" stroke="var(--band-3)" stroke-width="2"/></g>
      <g transform="translate(569,356)" filter="url(#hex-shadow)"><use href="#hex-outer" fill="#fff"/><use href="#hex-inner" fill="none" stroke="var(--band-4)" stroke-width="2"/></g>
      <g transform="translate(449,446)" filter="url(#hex-shadow)"><use href="#hex-outer" fill="#fff"/><use href="#hex-inner" fill="none" stroke="var(--band-5)" stroke-width="2"/></g>
      <g transform="translate(651,535)" filter="url(#hex-shadow)"><use href="#hex-outer" fill="#fff"/><use href="#hex-inner" fill="none" stroke="var(--band-6)" stroke-width="2"/></g>
      <g transform="translate(414,625)" filter="url(#hex-shadow)"><use href="#hex-outer" fill="#fff"/><use href="#hex-inner" fill="none" stroke="var(--band-7)" stroke-width="2"/></g>

      <rect x="393" y="64"  width="48" height="48" rx="4" fill="#d6edf2" role="img" aria-label="Computer screen with patient profile icon"/>
      <rect x="513" y="153" width="48" height="48" rx="4" fill="#dff0f8" role="img" aria-label="Labelled specimen tubes icon"/>
      <rect x="665" y="243" width="48" height="48" rx="4" fill="#d3eaef" role="img" aria-label="Linked data folders icon"/>
      <rect x="545" y="332" width="48" height="48" rx="4" fill="#d6ecf7" role="img" aria-label="Delivery truck icon"/>
      <g transform="translate(449,446)" fill="var(--band-5)">
        <path d="M-18,11 C-13,7 -13,2 -13,-7 C-13,-16 -7,-21 0,-21 C7,-21 13,-16 13,-7 C13,2 13,7 18,11 Z"/>
        <circle cx="0" cy="16" r="5.5"/>
        <circle cx="0" cy="-23" r="3"/>
      </g>
      <g transform="translate(651,535)" fill="none" stroke="var(--band-6)" stroke-width="2.5" stroke-linecap="round" stroke-linejoin="round">
        <rect x="-16" y="-20" width="32" height="43" rx="3"/>
        <rect x="-7" y="-24" width="14" height="8" rx="2" fill="#fff"/>
        <path d="M-10,-6 l3,3 l5,-6 M4,-5 h8 M-10,5 l3,3 l5,-6 M4,6 h8 M-10,16 l3,3 l5,-6 M4,17 h8"/>
      </g>
      <rect x="390" y="601" width="48" height="48" rx="4" fill="#d2e4e6" role="img" aria-label="Presenter at a results board icon"/>
    </svg>

    <div class="step" style="top:43px"><span class="step-num">01</span><p class="step-text">School/employer collects all <b>patient information</b><br>captured on a requisition form or electronically<br>(w signature) and DOES NOT send to VORTA</p></div>
    <div class="step" style="top:132.5px"><span class="step-num">02</span><p class="step-text">School/employer collects <b>individual specimens<br>and labels them</b> with a unique bar code<br>(non-repeating and can include the DOB)</p></div>
    <div class="step" style="top:222px"><span class="step-num">03</span><p class="step-text">School/employer is responsible for <b>housing and<br>managing</b> all the unique patient information for<br>each individual specimen</p></div>
    <div class="step" style="top:311.5px"><span class="step-num">04</span><p class="step-text">School/employer <b>delivers specimens</b> to VORTA and<br>School/employer directs VORTA what specimens are<br>in what designated pool (one pool size for entire project)</p></div>
    <div class="step" style="top:401px"><span class="step-num">05</span><p class="step-text">When a pool is <b>positive</b>,<br>VORTA notifies School/employer</p></div>
    <div class="step" style="top:490.5px"><span class="step-num">06</span><p class="step-text">When <b>reflex testing</b> in indicated for client,<br>School/employer submits to VORTA on demand<br>all patient information needed to process the reflexed option</p></div>
    <div class="step" style="top:580px"><span class="step-num">07</span><p class="step-text">VORTA reports back to School/employer<br>in <b>12 hours</b> the results of the retest</p></div>
  </section>

  <p class="refs">https://www.healthbureau-example.test/medical-devices/coronavirus-covid-19-and-medical-devices/pooled-sample-testing-and-screening-testing-covid-19<br>https://www.mediquestlabs.test/coronavirus-disease-covid-19/news/mediquest-receives-authorization-covid-19-sample-pooling</p>

  <footer class="footer">
    <svg width="804" height="55" viewBox="0 0 804 55">
      <polygon points="0,0 398,0 420,55 0,55" fill="var(--teal)"/>
      <polygon points="408,0 420,0 442,55 430,55" fill="var(--teal)"/>
      <g transform="translate(36,27)" fill="none" stroke="#fff" stroke-width="2">
        <circle r="10"/><ellipse rx="4.5" ry="10"/><path d="M-10,0 h20 M-8,-5 h16 M-8,5 h16"/>
      </g>
    </svg>
    <p class="phone">800-555-VRTA (8782) / 240-555-0187</p>
    <p class="web">
      <svg class="web-icon" width="32" height="32" viewBox="0 0 30 30"><polygon points="15,1 27,8 27,22 15,29 3,22 3,8" fill="#1c5f6e"/><g fill="none" stroke="#fff" stroke-width="1.5"><circle cx="15" cy="15" r="7"/><ellipse cx="15" cy="15" rx="3" ry="7"/><path d="M8,15 h14"/></g></svg>
      <span>www.vortadx.test</span>
    </p>
  </footer>

</div>
</body>
</html>
```